VARNO HOMES BRELT MARKETING FLYER

THE FLYER CAN BE FRONT TO BACK OR 2 PAGES IF NEEDED.

need to create a flyer with the following information:

Tallwick Co. is a CRM (Customer Relationship Management System) that provides leads to agents and a system to communicate and track your leads. Initial training and set up will be provided

Commission splits for leads are as follows: (maybe we can create a chart or box for items 1-3)

1. Cold leads 40% Varno - 60% Agent - Worked by Agent in the platform, agent shows property, writes contract, handles all negotiations and any necessary addendums, attends home inspection and settlement.

2. Warm leads 50% Varno - 50% Co-agent - Contacted by ISA, agent shows property, writes contract, handles all negotiations and any necessary addendums, attends home inspection and settlement.

3 Hot leads 70% Varno - 30% Co-agent - Prequalified by Varno Homes and ready to look at property, Varno writes contract and secures broker agency relationship agreements, co-agent shows property, , handles all negotiations (with support from VARNO if necessary), execute any necessary addendums, attend home inspection and settlement.

Preferred vendors such as Lender, Title, Insurance, Home Inspector, etc. are to be used for any transactions related to BRLT per Varno Homes.

Agents will receive 10 leads for free to start once Fresh Member Launchpad is complete. Warm leads will be available to purchase for $15 each beyond the first 10. Every 5 deals closed, agent commission will increase by 10% annually!!

Rules and restrictions apply.

3. In addition to Pennvale, a transaction coordinator included.

4. Free BRLT Support and training included

5. Free personal CRM website included

Industry/Entity Type

Real Estate

Colors
3176b5
85abd2
ecf5f6

Requirements
Must have
• everything in the description above

```html
<!DOCTYPE html>
<html lang="en">
<head>
<meta charset="utf-8">
<title>Varno Homes – BRLT Agent Flyer</title>
<link href="https://fonts.googleapis.com/css2?family=Roboto+Condensed:wght@700&family=Open+Sans:wght@400;600&display=swap" rel="stylesheet">
<style>
  :root {
    --navy: #0d2b63;
    --navy-deep: #0a2150;
    --blue: #1f56c0;
    --brand: #3176b5;
    --sky: #85abd2;
    --mist: #ecf5f6;
    --ink: #1b1b1b;
    --white: #ffffff;
  }
  * { box-sizing: border-box; margin: 0; padding: 0; }
  html, body { width: 900px; height: 1200px; overflow: hidden; background: var(--white); }
  body { font-family: "Open Sans", Arial, sans-serif; color: var(--ink); }

  .flyer { position: relative; width: 900px; height: 1200px; overflow: hidden; background: var(--white); }

  /* Masthead */
  .masthead {
    position: absolute; left: 0; top: 0; width: 900px; height: 170px;
    background: linear-gradient(180deg, #f4f6fa 0%, #e9edf3 100%);
    box-shadow: 0 4px 8px rgba(0,0,0,0.12);
    z-index: 2;
  }
  .brand {
    position: absolute; left: 0; right: 0; top: 58px;
    display: flex; justify-content: center; align-items: center; gap: 14px;
  }
  .brand-mark { width: 26px; height: 26px; background: var(--navy); }
  .brand-name {
    font-family: "Roboto Condensed", Arial Narrow, sans-serif; font-weight: 700;
    font-size: 48px; letter-spacing: 2px; color: var(--navy);
  }

  /* Hero */
  .hero {
    position: absolute; left: 0; top: 170px; width: 900px; height: 393px;
    background: linear-gradient(90deg, #f7f8fa 0%, #eef1f5 45%, #e8ecf1 100%);
  }
  .hero-photo {
    position: absolute; right: 0; top: 0; width: 490px; height: 393px;
    background: linear-gradient(120deg, #eef0f2 0%, #e8d6c6 40%, #d9a98a 62%, #f2f2f2 100%);
  }
  .hero-title {
    position: absolute; left: 42px; top: 210px;
    font-family: "Roboto Condensed", Arial Narrow, sans-serif; font-weight: 700;
    font-size: 58px; line-height: 1; color: var(--navy); letter-spacing: 0.5px;
  }
  .hero-band {
    position: absolute; left: 36px; top: 260px; width: 400px; height: 48px;
    background: var(--blue);
    font-family: "Roboto Condensed", Arial Narrow, sans-serif; font-weight: 700;
    font-size: 40px; line-height: 48px; color: var(--white); padding-left: 6px; letter-spacing: 0.5px;
  }
  .hero-sub {
    position: absolute; left: 46px; top: 314px;
    font-family: Arial, Helvetica, sans-serif; font-weight: 700; font-size: 22px; color: var(--ink);
  }

  /* Info columns */
  .info-strip { position: absolute; left: 0; top: 563px; width: 900px; height: 173px; display: flex; }
  .info-col {
    height: 100%; display: flex; align-items: center; justify-content: center;
    color: var(--white); font-size: 14.5px; line-height: 1.32; text-align: justify; padding: 0 22px;
    background: linear-gradient(180deg, #123573 0%, var(--navy-deep) 100%);
  }
  .info-col p { width: 100%; }
  .info-col.is-crm { width: 338px; padding-left: 42px; }
  .info-col.is-leads { width: 294px; background: var(--blue); text-align: center; padding: 0 16px; }
  .info-col.is-vendors { width: 268px; padding-right: 18px; }

  /* Commission */
  .commission {
    position: absolute; left: 0; top: 736px; width: 900px; height: 404px;
    background: linear-gradient(180deg, #ffffff 0%, #f3f4f7 45%, #e4e7ec 100%);
  }
  .commission-title {
    position: absolute; left: 0; right: 0; top: 28px; text-align: center;
    font-weight: 600; font-size: 31px; color: var(--ink);
  }
  .commission-title span { color: var(--blue); }
  .commission-note { position: absolute; left: 0; right: 0; top: 68px; text-align: center; font-size: 18px; }
  .split { position: absolute; font-size: 12px; line-height: 1.38; text-align: justify; color: var(--ink); }
  .split.is-hot { left: 44px; top: 100px; width: 816px; }
  .split.is-cold { left: 44px; top: 162px; width: 400px; }
  .split.is-warm { left: 474px; top: 154px; width: 386px; padding-left: 10px; border-left: 1px solid #b9bfc9; }

  .divider { position: absolute; left: 22px; top: 226px; width: 856px; height: 20px; }

  .rules-title {
    position: absolute; left: 0; right: 0; top: 272px; text-align: center;
    font-size: 24px; font-weight: 600; color: var(--ink);
  }
  .rules-title span { color: var(--blue); }

  .perks { position: absolute; left: 60px; top: 316px; width: 800px; display: flex; justify-content: space-between; }
  .perk { display: flex; align-items: flex-start; gap: 14px; font-size: 13.5px; line-height: 1.35; width: 250px; }
  .perk + .perk { border-left: 1px solid #c4c9d2; padding-left: 14px; }
  .perk svg { flex: none; width: 30px; height: 30px; }

  /* Footer */
  .footer { position: absolute; left: 0; top: 1140px; width: 900px; height: 60px; display: flex; }
  .footer-call {
    width: 432px; background: var(--blue); color: var(--white);
    font-family: Arial, Helvetica, sans-serif; font-size: 21px; line-height: 60px; padding-left: 78px;
  }
  .footer-web {
    flex: 1; background: var(--navy-deep); color: var(--white);
    font-family: Arial, Helvetica, sans-serif; font-size: 21px; line-height: 60px; padding-left: 56px; letter-spacing: 1.5px;
  }
</style>
</head>
<body>
<main class="flyer">

  <header class="masthead">
    <div class="brand">
      <span class="brand-mark"></span>
      <span class="brand-name">VARNO HOMES</span>
    </div>
  </header>

  <section class="hero">
    <div class="hero-photo" role="img" aria-label="Photo of a happy family: mother, father and young daughter on his shoulders, laughing in a bright home"></div>
    <h1 class="hero-title">VARNO HOMES</h1>
    <div class="hero-band">IS A DYNAMIC AND</div>
    <p class="hero-sub">multi-cultural group of real estate</p>
  </section>

  <section class="info-strip">
    <div class="info-col is-crm">
      <p>Tallwick Co. is a CRM (Customer Relationship Management System) that provides leads to agents and a system to communicate and track your leads. Initial training and set up will be provided</p>
    </div>
    <div class="info-col is-leads">
      <p>Agents will receive 10 leads for free to start once Fresh Member Launchpad is complete. Warm leads will be available to purchase for $15 each beyond the first 10. Every 5 deals closed, agent commission will increase by 10% annually!!</p>
    </div>
    <div class="info-col is-vendors">
      <p>Preferred vendors such as Lender, Title, Insurance, Home Inspector, etc. are to be used for any transactions related to BRLT per Varno Homes.</p>
    </div>
  </section>

  <section class="commission">
    <h2 class="commission-title">Commission <span>splits for leads</span> are as follows:</h2>
    <p class="commission-note">(maybe we can create a chart or box for items 1-3)</p>

    <p class="split is-hot">Hot leads 70% Varno - 30% Co-agent - Prequalified by Varno Homes and ready to look at property, Varno writes contract and secures broker agency relationship agreements, co-agent shows property, , handles all negotiations (with support from VARNO if necessary), execute any necessary addendums, attend home inspection and settlement.</p>
    <p class="split is-cold">Cold leads 40% Varno - 60% Agent - Worked by Agent in the platform, agent shows property, writes contract, handles all negotiations and any necessary addendums, attends home inspection and settlement.</p>
    <p class="split is-warm">Warm leads 50% Varno - 50% Co-agent - Contacted by ISA, agent shows property, writes contract, handles all negotiations and any necessary addendums, attends home inspection and settlement.</p>

    <svg class="divider" viewBox="0 0 856 20" preserveAspectRatio="none" aria-hidden="true">
      <polygon points="0,0 856,0 836,20 20,20" fill="#0a2150"/>
    </svg>

    <h2 class="rules-title">Rules and <span>restrictions</span> apply</h2>

    <ul class="perks">
      <li class="perk">
        <svg viewBox="0 0 30 30" aria-hidden="true"><circle cx="15" cy="15" r="13.5" fill="none" stroke="#0d2b63" stroke-width="1.5"/><path d="M8 15 L15 8.5 L22 15 L20 15 L20 21 L16.5 21 L16.5 17 L13.5 17 L13.5 21 L10 21 L10 15 Z" fill="#0d2b63"/></svg>
        <span>Free BRLT Support and training included</span>
      </li>
      <li class="perk">
        <svg viewBox="0 0 30 30" aria-hidden="true"><circle cx="15" cy="15" r="13.5" fill="none" stroke="#0d2b63" stroke-width="1.5"/><path d="M8 15 L15 8.5 L22 15 L20 15 L20 21 L16.5 21 L16.5 17 L13.5 17 L13.5 21 L10 21 L10 15 Z" fill="#0d2b63"/></svg>
        <span>Free personal CRM website included</span>
      </li>
      <li class="perk">
        <svg viewBox="0 0 30 30" aria-hidden="true"><circle cx="15" cy="15" r="13.5" fill="none" stroke="#0d2b63" stroke-width="1.5"/><path d="M8 15 L15 8.5 L22 15 L20 15 L20 21 L16.5 21 L16.5 17 L13.5 17 L13.5 21 L10 21 L10 15 Z" fill="#0d2b63"/></svg>
        <span>In addition to Pennvale, a transaction coordinator included</span>
      </li>
    </ul>
  </section>

  <footer class="footer">
    <div class="footer-call">CALL US- +1 555-014-2270</div>
    <div class="footer-web">VISIT - www.varnohomes.net</div>
  </footer>

</main>
</body>
</html>
```